Larkfield Clinic Marketing Flyer

We are a new medical practice in the community and need a flyer to send to other medical offices to inform of our services. We just completed our logo with PixelGuild and would like to incorporate that plus our marketing content into the flyer. Our medical practice has 2 divisions: (1)Mental Health/Psychiatry and (2) Migraine and Neurospasticity Management. Please see website for content and provider photos at www.LarkfieldCare.example

Target Market(s)

Other Healthcare Professionals in the Community

Industry/Entity Type

Medical

Requirements
Must have
• Photos of all 5 healthcare providers, phone number, address, logo

```html
<!DOCTYPE html>
<html lang="en">
<head>
<meta charset="utf-8">
<title>Larkfield Clinic Flyer</title>
<link href="https://fonts.googleapis.com/css2?family=Roboto:wght@400;500;700&display=swap" rel="stylesheet">
<style>
  :root {
    --teal: #1b9384;
    --teal-bright: #22b4a0;
    --lime: #a9cc52;
    --white: #ffffff;
    --page: #d3d3d3;
    --photo-a: #4a5559;
    --photo-b: #2c3538;
  }
  * { margin: 0; padding: 0; box-sizing: border-box; }
  html, body { width: 1200px; height: 1200px; overflow: hidden; }
  body { background: var(--page); font-family: "Roboto", Arial, sans-serif; position: relative; }
  .flyer { position: absolute; left: 204px; top: 40px; width: 792px; height: 1120px; background: var(--teal); overflow: hidden; color: var(--white); }
  .flyer > * { position: absolute; }
  .diagonal { left: 0; top: 0; width: 792px; height: 1120px; }
  .headline { left: 41px; top: 36px; font-weight: 700; font-size: 71px; line-height: 64px; letter-spacing: -0.5px; }
  .services { left: 42px; top: 242px; font-size: 24px; line-height: 24px; }
  .accent-bar { left: 41px; top: 306px; width: 178px; height: 9px; background: var(--lime); }
  .logo-ring { left: 521px; top: 36px; width: 242px; height: 242px; border-radius: 50%; background: var(--lime); }
  .logo-disc { left: 514px; top: 40px; width: 232px; height: 232px; border-radius: 50%; background: var(--white);
    display: flex; align-items: center; justify-content: center; }
  .logo-name { color: var(--teal); font-size: 25px; font-weight: 500; }
  .section-label { left: 41px; height: 47px; background: var(--white); border-radius: 8px; color: var(--teal);
    font-weight: 700; font-size: 27px; line-height: 47px; padding-left: 23px; }
  .label-providers { top: 344px; width: 470px; }
  .label-migraine { top: 689px; width: 583px; }
  .body-copy { font-size: 15.5px; line-height: 18.7px; }
  .copy-providers { left: 68px; top: 409px; width: 670px; }
  .copy-migraine { left: 217px; top: 761px; width: 505px; }
  .card { width: 128px; height: 188px; background: var(--teal); border-radius: 12px; }
  .card-photo { position: absolute; left: 8px; top: 10px; width: 112px; height: 137px;
    background: radial-gradient(circle at 50% 40%, var(--photo-a), var(--photo-b)); }
  .card-name { position: absolute; left: 0; right: 0; top: 150px; text-align: center; color: var(--lime);
    font-weight: 700; font-size: 13px; line-height: 14.5px; }
  .footer-stripe { left: 0; top: 960px; width: 792px; height: 8px; background: var(--teal-bright); }
  .footer-band { left: 0; top: 968px; width: 792px; height: 88px; background: var(--teal); }
  .phone-tab { left: 315px; top: 918px; width: 434px; height: 70px; background: var(--lime); border-radius: 0 0 10px 10px;
    font-weight: 700; font-size: 56px; line-height: 70px; text-align: center; color: var(--white); }
  .contact { left: 65px; font-size: 23px; }
  .contact b { font-weight: 700; }
  .contact-address { top: 988px; }
  .contact-email { top: 1020px; }
  .website { left: 0; width: 792px; top: 1066px; text-align: center; color: var(--teal); font-size: 22px; }
</style>
</head>
<body>
  <main class="flyer">
    <svg class="diagonal" viewBox="0 0 792 1120"><polygon points="0,536 792,259 792,1120 0,1120" fill="var(--lime)"/></svg>

    <h1 class="headline">Helping Bodies<br>Helping Minds<br>Helping You</h1>
    <p class="services">Mental Health and Psychiatry Services<br>Migraine and Neurospasticity Intervention</p>
    <div class="accent-bar"></div>

    <div class="logo-ring"></div>
    <div class="logo-disc"><span class="logo-name">Larkfield Clinic</span></div>

    <h2 class="section-label label-providers">Meet Our Mental Health Providers</h2>
    <p class="body-copy copy-providers">Bringing comprehensive evaluation, medication management and psychotherapy to the full spectrum of mental health disorders including minor, moderate and major depression, bipolar disorder, ADD/ADHD, anxiety, schizophrenia, stress or grief reactions, and others.</p>

    <div class="card" style="left:68px;top:482px"><div class="card-photo" role="img" aria-label="Portrait of Evan Marlow"></div><p class="card-name">Evan Marlow,<br>PMHNP - BC</p></div>
    <div class="card" style="left:248px;top:482px"><div class="card-photo" role="img" aria-label="Portrait of Dana Whitfield"></div><p class="card-name">Dana Whitfield,<br>PMHNP - BC</p></div>
    <div class="card" style="left:427px;top:482px"><div class="card-photo" role="img" aria-label="Portrait of Colin Ashby"></div><p class="card-name">Colin Ashby<br>PMHNP - BC</p></div>
    <div class="card" style="left:605px;top:482px"><div class="card-photo" role="img" aria-label="Portrait of Miriam Holt"></div><p class="card-name">Miriam Holt,<br>PMHNP-BC</p></div>

    <h2 class="section-label label-migraine">Migraine and Neurospasticity Intervention</h2>
    <div class="card" style="left:68px;top:758px"><div class="card-photo" role="img" aria-label="Portrait of Dr. Paul R. Kessler" style="background:linear-gradient(180deg,#9a6a3e,#c9b9a0)"></div><p class="card-name">Dr. Paul R.<br>Kessler</p></div>
    <p class="body-copy copy-migraine">Injections of botulinum neurotoxin are a widely used therapeutic form of treatment for both chronic migraines and patients with involuntary muscle contractions (neurospasticity). Injections may offer up to 3 months of relief and may be combined with other pharmaceutical interventions for maximum benefit.</p>

    <div class="footer-stripe"></div>
    <div class="footer-band"></div>
    <div class="phone-tab">555-014-2286</div>
    <p class="contact contact-address"><b>Address:</b> 1250 Meadowbrook Ln, Suite B Springdale, ID 83800</p>
    <p class="contact contact-email"><b>Email:</b> hello@LarkfieldCare.example</p>
    <p class="website">www.LarkfieldCare.example</p>
  </main>
</body>
</html>
```